Custom Real Estate Postcard for Buying Communities

We are a real estate company that owns/operates mobile home parks and want to send out a postcard to owners of these communities letting them know who our company is and let them know we want to buy their community. We are looking to create a postcard that introduces our company to the owner and also lets them know we want to buy their community - we are targeting older mom & pop type communities so we would like the postcard to have a home-y feel that makes the owner feel like our company will treat them fairly during the acquisition process
I have attached a few images from our communities that might look good on a postcard - you don't need to use all of them, I just included multiple so there are different options. please feel free to edit/enhance the images if needed.
Our company is Bright Meadow Holdings (BMH) and the logo is attached.
Text to be included somewhere on postcard: "We pride ourselves on active hands-on management in order to provide our residents quality communities at an affordable price.
BMH is a proven owner/operator and has the ability to purchase without any financing contingencies.
We provide a quick and easy closing. We do not retrade
Target Market(s)
Owners of Mobile Home Parks that BMH (our company) would like to acquire - small mom & pop owners that want to see that we aren't the big firm trying to come in and take over but a local company that will still treat the residents well
Industry/Entity Type
Real Estate
Colors
Designer to choose colors to be used in the design.
Requirements
Must have
- The BMH logo, at least one picture of a mobile home park from the attached pictures. And some version/form of the provided text. Info/contact section with website (www.bmhparks.example), email (info@bmhparks.example) and phone (555.284.7160)
- Something sort of call to action like: "We Want to Buy Your Community", "Ready to Sell?", "Interested in Selling?" etc.
Nice to have
- BMH Logo Colors, in addition to any other colors if designer thinks there are complimentary colors

```html
<!DOCTYPE html>
<html lang="en">
<head>
<meta charset="utf-8">
<title>Bright Meadow Holdings – Postcard</title>
<link href="https://fonts.googleapis.com/css2?family=Roboto+Condensed:wght@400;700&family=Roboto:wght@400;500&display=swap" rel="stylesheet">
<style>
  :root {
    --brown: #7a2d16;
    --brown-dark: #4b2a10;
    --gold: #a77b2d;
    --gold-light: #c9a25a;
    --red-text: #9b2a17;
    --ink: #2b2b2b;
    --page: #d8d8d8;
    --paper: #ffffff;
    --rule: #8d8d8d;
  }
  * { box-sizing: border-box; margin: 0; padding: 0; }
  html, body { width: 1200px; height: 1116px; overflow: hidden; }
  body { background: var(--page); position: relative; font-family: "Roboto Condensed", Arial, sans-serif; color: var(--ink); }

  .card {
    position: absolute; left: 200px; width: 800px; height: 514px;
    background: var(--paper); overflow: hidden;
    box-shadow: 0 6px 14px rgba(0,0,0,.28);
  }
  .card--front { top: 29px; }
  .card--back { top: 573px; }
  .card__art { position: absolute; inset: 0; }

  .brand { position: absolute; display: flex; align-items: center; gap: 12px; }
  .brand__mark { width: 40px; height: 40px; background: var(--brown); }
  .brand__name {
    font-family: "Roboto Condensed", sans-serif; font-weight: 400;
    text-transform: uppercase; letter-spacing: 1px; color: var(--brown-dark); line-height: 1.05;
  }
  .card--front .brand { left: 28px; top: 28px; }
  .card--front .brand__name { font-size: 18px; }
  .card--back .brand { left: 84px; top: 24px; }
  .card--back .brand__mark { width: 48px; height: 48px; }
  .card--back .brand__name { font-size: 22px; }

  .intro {
    position: absolute; left: 29px; top: 354px; width: 478px;
    font-size: 17.5px; line-height: 22px; text-align: justify; color: var(--ink);
  }
  .intro__name { color: var(--brown); font-weight: 700; }
  .intro__abbr { color: var(--brown); }

  .site-band {
    position: absolute; left: 0; right: 0; bottom: 0; height: 42px;
    background: var(--brown); color: #fff;
    font-family: "Roboto", sans-serif; font-size: 21px; font-weight: 500;
    display: flex; align-items: center; justify-content: center; letter-spacing: .3px;
  }

  .offer-tab {
    position: absolute; left: 129px; top: 262px; width: 165px; height: 22px;
    background: var(--brown); color: #fff; font-size: 17px;
    display: flex; align-items: center; justify-content: center;
  }
  .offer-bar {
    position: absolute; left: 12px; top: 284px; width: 400px; height: 28px;
    background: var(--gold); color: #fff; font-size: 12.5px;
    display: flex; align-items: center; justify-content: center;
    box-shadow: 0 2px 3px rgba(0,0,0,.25);
  }
  .sell-prompt {
    position: absolute; left: 68px; top: 328px; width: 300px;
    text-align: center; color: var(--red-text); font-size: 12.5px; line-height: 16px;
  }
  .contact { position: absolute; left: 24px; top: 366px; }
  .contact__phone { display: flex; align-items: center; gap: 6px; font-size: 19px; font-weight: 700; color: var(--ink); }
  .contact__line { display: flex; align-items: center; gap: 8px; font-size: 12.5px; margin-top: 3px; padding-left: 3px; }
  .contact__line:first-of-type { margin-top: 5px; }
  .social { position: absolute; left: 236px; top: 370px; }
  .social__label { font-size: 15px; font-weight: 700; color: var(--ink); }
  .social__dots { display: flex; gap: 8px; margin-top: 5px; margin-left: 3px; }
  .social__dot { width: 21px; height: 21px; border: 1.5px solid var(--ink); border-radius: 50%; }

  .stamp-box { position: absolute; left: 674px; top: 31px; width: 93px; height: 93px; border: 1px solid var(--rule); }
  .address-line { position: absolute; left: 527px; width: 240px; height: 0; border-top: 1px solid var(--rule); }
</style>
</head>
<body>

  <!-- Front of postcard -->
  <section class="card card--front">
    <svg class="card__art" width="800" height="514" viewBox="0 0 800 514">
      <defs>
        <linearGradient id="heroFill" x1="0" y1="0" x2="0" y2="1">
          <stop offset="0" stop-color="#6fa8e0"/>
          <stop offset=".35" stop-color="#a7c4dc"/>
          <stop offset=".6" stop-color="#5f6f4a"/>
          <stop offset="1" stop-color="#3e4d33"/>
        </linearGradient>
        <linearGradient id="homeA" x1="0" y1="0" x2="0" y2="1">
          <stop offset="0" stop-color="#6a8c4a"/>
          <stop offset=".5" stop-color="#d8cdb6"/>
          <stop offset="1" stop-color="#7b8f4b"/>
        </linearGradient>
        <linearGradient id="homeB" x1="0" y1="0" x2="0" y2="1">
          <stop offset="0" stop-color="#4f8fd6"/>
          <stop offset=".5" stop-color="#e7ece8"/>
          <stop offset="1" stop-color="#8f9a4a"/>
        </linearGradient>
      </defs>
      <rect role="img" aria-label="Photo of a manufactured home with white porch and railing among trees" x="0" y="0" width="800" height="340" fill="url(#heroFill)"/>
      <path d="M0,262 Q330,372 800,218 L800,236 Q330,390 0,292 Z" fill="var(--gold)"/>
      <path d="M0,292 Q330,390 800,236 L800,514 L0,514 Z" fill="var(--paper)"/>
      <g role="img" aria-label="Photo of a beige manufactured home with a paved drive">
        <circle cx="694" cy="321" r="82" fill="url(#homeA)" stroke="#1e1e1e" stroke-width="3"/>
      </g>
      <g role="img" aria-label="Photo of a white manufactured home on a grassy lot">
        <circle cx="594" cy="386" r="64" fill="url(#homeB)" stroke="#1e1e1e" stroke-width="3"/>
      </g>
    </svg>

    <div class="brand">
      <span class="brand__mark"></span>
      <span class="brand__name">Bright Meadow<br>Holdings</span>
    </div>

    <p class="intro">
      <span class="intro__name">Bright Meadow Holdings</span> <span class="intro__abbr">(BMH)</span> is a proven owner/operator
      of Manufactured Housing communities and is actively looking for communities to acquire. BMH takes
      pride in hands-on management and has the ability to purchase without any financing contingencies.
    </p>

    <div class="site-band">www.bmhparks.example</div>
  </section>

  <!-- Back of postcard -->
  <section class="card card--back">
    <svg class="card__art" width="800" height="514" viewBox="0 0 800 514">
      <defs>
        <clipPath id="panelClip">
          <path d="M0,0 L376,0 Q500,230 350,432 L0,432 Z"/>
        </clipPath>
        <linearGradient id="panelFill" x1="0" y1="0" x2="1" y2="0">
          <stop offset="0" stop-color="#eeeeee"/>
          <stop offset="1" stop-color="#ffffff"/>
        </linearGradient>
        <linearGradient id="aerialFill" x1="0" y1="0" x2="1" y2="1">
          <stop offset="0" stop-color="#3f6b2c"/>
          <stop offset=".5" stop-color="#8a9a6e"/>
          <stop offset="1" stop-color="#2f5a24"/>
        </linearGradient>
      </defs>
      <g clip-path="url(#panelClip)">
        <rect x="0" y="0" width="480" height="432" fill="url(#panelFill)"/>
        <rect x="0" y="0" width="480" height="100" fill="var(--paper)"/>
        <rect role="img" aria-label="Aerial photo of a manufactured home community surrounded by trees" x="0" y="100" width="480" height="152" fill="url(#aerialFill)"/>
      </g>
      <path d="M376,0 Q500,230 350,432" fill="none" stroke="var(--brown-dark)" stroke-width="6"/>
      <path d="M369,0 Q492,230 344,432" fill="none" stroke="var(--gold-light)" stroke-width="2"/>
    </svg>

    <div class="brand">
      <span class="brand__mark"></span>
      <span class="brand__name">Bright Meadow<br>Holdings</span>
    </div>

    <div class="offer-tab">We Offer</div>
    <div class="offer-bar">A quick due diligence and closing time line and we do not retrade.</div>
    <p class="sell-prompt">Please contact us if you are interested in<br>selling your community</p>

    <div class="contact">
      <div class="contact__phone">
        <svg width="15" height="15" viewBox="0 0 16 16" aria-hidden="true"><circle cx="8" cy="8" r="8" fill="var(--brown)"/><path d="M5,4 L7,4 L7.6,6 L6.6,7 Q7.5,8.8 9,9.4 L10,8.4 L12,9 L12,11 Q7,12 4.6,6 Z" fill="#fff"/></svg>
        <span>555.284.7160</span>
      </div>
      <div class="contact__line">
        <svg width="9" height="7" viewBox="0 0 9 7" aria-hidden="true"><rect width="9" height="7" fill="var(--brown)"/><path d="M0,0 L4.5,4 L9,0" fill="none" stroke="#fff" stroke-width="1"/></svg>
        <span>info@bmhparks.example</span>
      </div>
      <div class="contact__line">
        <svg width="9" height="9" viewBox="0 0 9 9" aria-hidden="true"><circle cx="4.5" cy="4.5" r="4.5" fill="var(--brown)"/></svg>
        <span>www.bmhparks.example</span>
      </div>
    </div>

    <div class="social">
      <div class="social__label">Get in touch</div>
      <div class="social__dots"><span class="social__dot"></span><span class="social__dot"></span><span class="social__dot"></span></div>
    </div>

    <div class="stamp-box"></div>
    <div class="address-line" style="top:215px"></div>
    <div class="address-line" style="top:259px"></div>
    <div class="address-line" style="top:301px"></div>
    <div class="address-line" style="top:343px"></div>
  </section>

</body>
</html>
```